Veteran Owned General Contractor needs Bold New Business Cards

We are a service disabled veteran owned small business. We're a general contractor that specializes in excavation, underground utilities, site work, land clearing and demolition. We would like a fresh, simple, bold, new look for our business cards. We're open to ideas! We'd like to incorporate the following information on the card:

Company Name & Logo, Name of Person, Job Title, Office Phone, Fax, Cell Phone, Email Address, Website, SDVOSB

Our logo is included. We look forward to your thoughts.

Thank you!
Updates

Reason: Hello Due to the overwhelming response to this project, we are extending the deadline one time to allow for improved communication and feedback with the top candidates. We would like to thank everyone for their hard work and exceptional creativity! Thank you

Industry/Entity Type

Business

Contact Information for Business Card

Font styles to use
Sans Serif

Requirements
Nice to have
• As we are a veteran owned company, it would be nice to incorporate an American flag into the design. Maybe on the back?

```html
<!DOCTYPE html>
<html lang="en">
<head>
<meta charset="utf-8">
<title>Bedrock9 Business Card</title>
<link rel="stylesheet" href="https://fonts.googleapis.com/css2?family=Montserrat:wght@400;500;700;800&display=swap">
<style>
  :root {
    --bg: #2a1a12;
    --card-white: #ffffff;
    --card-dark: #161616;
    --green: #6cc04a;
    --gray: #8c8c8c;
    --ink: #161616;
    --light: #e6e6e6;
    --flag-red: #b22234;
    --flag-blue: #3c3b6e;
  }
  html, body {
    margin: 0;
    width: 1200px;
    height: 1000px;
    overflow: hidden;
    background: var(--bg);
    font-family: "Montserrat", sans-serif;
  }
  .canvas { position: relative; width: 1200px; height: 1000px; }
  .card {
    position: absolute;
    width: 540px;
    height: 310px;
    overflow: hidden;
    box-shadow: 0 10px 24px rgba(0,0,0,0.45);
  }
  .card-front { left: 330px; top: 120px; background: var(--card-white); }
  .card-back { left: 330px; top: 540px; background: var(--card-dark); }
  .front-shapes { position: absolute; inset: 0; }
  .brand-block {
    position: absolute; right: 28px; top: 26px; text-align: right;
  }
  .brand {
    display: flex; align-items: center; justify-content: flex-end; gap: 8px;
    font-weight: 800; font-size: 26px; color: var(--green); letter-spacing: 0.5px;
  }
  .brand-square { width: 22px; height: 22px; background: var(--ink); border-radius: 3px; }
  .person-name { margin-top: 6px; font-weight: 700; font-size: 20px; color: var(--ink); }
  .person-name .surname { color: var(--green); }
  .person-title { font-size: 14px; color: var(--ink); }
  .badge-label {
    position: absolute; left: 16px; top: 173px;
    font-size: 14px; color: var(--light); letter-spacing: 0.5px;
  }
  .contact-list {
    position: absolute; margin: 0; padding: 0; list-style: none;
    font-size: 11.5px; color: var(--light); line-height: 18px;
  }
  .phones { left: 36px; top: 232px; }
  .details { left: 345px; top: 176px; }
  .contact-list li { display: flex; align-items: flex-start; gap: 10px; }
  .contact-list svg { flex: none; width: 11px; height: 11px; margin-top: 3px; fill: var(--green); }
  .back-marks {
    position: absolute; inset: 0;
    display: flex; align-items: center; justify-content: center; gap: 26px;
  }
  .back-brand {
    display: flex; align-items: center; gap: 10px;
    font-weight: 800; font-size: 28px; color: var(--green);
  }
  .back-brand .brand-square { width: 26px; height: 26px; background: var(--gray); }
  .flag-disc {
    width: 108px; height: 108px; border-radius: 50%;
    background: linear-gradient(135deg, var(--flag-blue) 0%, var(--flag-blue) 40%, var(--flag-red) 60%, #e8e8e8 100%);
  }
</style>
</head>
<body>
<main class="canvas">
  <section class="card card-front">
    <svg class="front-shapes" viewBox="0 0 540 310" width="540" height="310" aria-hidden="true">
      <polygon points="360,142 540,142 540,158 350,158" fill="var(--gray)"/>
      <polygon points="0,208 328,208 350,158 540,158 540,310 0,310" fill="var(--card-dark)"/>
      <polygon points="0,195 338,195 333,208 0,208" fill="var(--green)"/>
      <polygon points="0,168 112,168 128,195 0,195" fill="var(--card-dark)"/>
    </svg>

    <div class="brand-block">
      <div class="brand"><span class="brand-square"></span>BEDROCK9</div>
      <div class="person-name">JOHN <span class="surname">DOE</span></div>
      <div class="person-title">General Manager</div>
    </div>

    <div class="badge-label">SDVOSB</div>

    <ul class="contact-list phones">
      <li><svg viewBox="0 0 12 12"><rect x="3" y="0" width="6" height="12" rx="1"/></svg>01 234 456 7898</li>
      <li><svg viewBox="0 0 12 12"><path d="M2 0l3 3-1.5 1.5a7 7 0 0 0 4 4L9 7l3 3-2 2C5 12 0 7 0 2z"/></svg>01 234 456 7898</li>
      <li><svg viewBox="0 0 12 12"><rect x="3" y="0" width="6" height="4"/><rect x="0" y="4" width="12" height="5" rx="1"/><rect x="3" y="8" width="6" height="4"/></svg>01 234 456 7898</li>
    </ul>

    <ul class="contact-list details">
      <li><svg viewBox="0 0 12 12"><rect x="0" y="2" width="12" height="8" rx="1"/></svg>emailaddress@domain.com</li>
      <li><svg viewBox="0 0 12 12"><circle cx="6" cy="6" r="6"/></svg>www.yourwebsite.com</li>
      <li><svg viewBox="0 0 12 12"><path d="M6 0a4 4 0 0 1 4 4c0 3-4 8-4 8S2 7 2 4a4 4 0 0 1 4-4z"/></svg>2140 Ridgeway Lane<br>Hampton, VA 23661</li>
    </ul>
  </section>

  <section class="card card-back">
    <div class="back-marks">
      <div class="back-brand"><span class="brand-square"></span>BEDROCK9</div>
      <div class="flag-disc" role="img" aria-label="Round American flag emblem"></div>
    </div>
  </section>
</main>
</body>
</html>
```